Boutique Sparkling Blanc de Blancs Wine label

We are looking for a label and neck label for our new Sparkling Chardonnay.
Images uploaded include, bubbles and glitter maybe as a faded background for whole label?
We like Refined, elegant yet simple designs.
Have included our current table chardonnay label as example.

Industry/Entity Type

Boutique

Font styles to use
Decorative
Script

Requirements
Must have
• Name - "Every Moonlit Hour"
• Methode Traditionelle
• Blanc de Blancs
• 2015
• Beyond the Orchards (Brand)
• Adelaide Hills
Nice to have
• Neutral tones
• Sparkles, Glitter, Bubbles
• Traditional, cursive or vine like fonts
• Have attached fonts we used for previous wine label - might be nice to carry through same/similar fonts to continue our brand?
Should not have
• a lot of colour

```html
<!DOCTYPE html>
<html lang="en">
<head>
<meta charset="utf-8">
<title>Every Moonlit Hour – Label Options</title>
<link rel="stylesheet" href="https://fonts.googleapis.com/css2?family=Allura&family=Cinzel:wght@400;500&display=swap">
<style>
  :root {
    --canvas: #ffffff;
    --label-paper: #ffffff;
    --label-ground: #2c2a29;
    --frame-line: #9a9a9a;
    --glitter-light: #e4e4e4;
    --glitter-mid: #a9a9a9;
    --text-muted: #b9b4ad;
    --text-bright: #ffffff;
    --vine-dark: #0e0d0d;
    --vine-soft: #6d6a68;
  }
  html, body {
    margin: 0;
    padding: 0;
    overflow: hidden;
  }
  body {
    width: 1200px;
    height: 1000px;
    background: var(--canvas);
    position: relative;
  }
  .label {
    position: absolute;
    top: 134px;
    width: 584px;
    height: 668px;
    background: var(--label-paper);
    border: 1px solid var(--frame-line);
    box-shadow: 3px 3px 4px rgba(0, 0, 0, 0.35);
    box-sizing: border-box;
  }
  .label--dark-vines { left: 10px; }
  .label--soft-vines { left: 608px; }

  .label__ground {
    position: absolute;
    background: var(--label-ground);
    overflow: hidden;
  }
  .label--dark-vines .label__ground { left: 5px; top: 6px; right: 4px; bottom: 2px; }
  .label--soft-vines .label__ground { left: 11px; top: 13px; right: 9px; bottom: 12px; }

  .wine-name,
  .vintage {
    position: absolute;
    left: 0;
    right: 0;
    text-align: center;
    font-family: "Allura", cursive;
    color: var(--glitter-mid);
    background: linear-gradient(180deg, var(--glitter-light), var(--glitter-mid) 55%, var(--glitter-light));
    -webkit-background-clip: text;
    background-clip: text;
    -webkit-text-fill-color: transparent;
    line-height: 1;
  }
  .wine-name {
    top: 62px;
    font-size: 72px;
    letter-spacing: 1px;
  }
  .vintage {
    top: 540px;
    font-size: 92px;
    letter-spacing: 4px;
  }

  .wine-details {
    position: absolute;
    left: 0;
    right: 0;
    top: 288px;
    text-align: center;
    font-family: "Cinzel", serif;
    color: var(--text-muted);
    line-height: 1.25;
  }
  .label--soft-vines .wine-details { color: var(--text-bright); top: 280px; }
  .wine-details p { margin: 0; }
  .wine-details__style { font-size: 24px; }
  .wine-details__producer { font-size: 23px; margin-top: 38px !important; }
  .wine-details__region { font-size: 19px; }
  .label--soft-vines .wine-details__region { font-size: 22px; }

  .vine-ornament {
    position: absolute;
    border-radius: 45%;
  }
  .label--dark-vines .vine-ornament {
    background: radial-gradient(ellipse at center, rgba(14, 13, 13, 0.85), rgba(14, 13, 13, 0) 72%);
  }
  .label--soft-vines .vine-ornament {
    background: radial-gradient(ellipse at center, rgba(109, 106, 104, 0.55), rgba(109, 106, 104, 0) 72%);
  }
  .vine-ornament--upper-left { left: -10px; top: 160px; width: 230px; height: 170px; }
  .vine-ornament--lower-right { right: -10px; top: 415px; width: 230px; height: 200px; }
  .vine-ornament--lower-left { left: -10px; top: 600px; width: 170px; height: 90px; }
</style>
</head>
<body>

  <section class="label label--dark-vines">
    <div class="label__ground">
      <div class="vine-ornament vine-ornament--upper-left" role="img" aria-label="Black curling vine tendril ornament"></div>
      <div class="vine-ornament vine-ornament--lower-right" role="img" aria-label="Black curling vine tendril ornament"></div>
      <div class="vine-ornament vine-ornament--lower-left" role="img" aria-label="Black curling vine tendril ornament"></div>
      <h1 class="wine-name" style="margin:0;font-weight:400;">Every Moonlit Hour</h1>
      <div class="wine-details">
        <p class="wine-details__style">Methode Traditionelle</p>
        <p class="wine-details__style">Blanc de Blancs</p>
        <p class="wine-details__producer">Beyond the Orchards</p>
        <p class="wine-details__region">Adelaide Hills</p>
      </div>
      <div class="vintage">2015</div>
    </div>
  </section>

  <section class="label label--soft-vines">
    <div class="label__ground">
      <div class="vine-ornament vine-ornament--upper-left" role="img" aria-label="Grey curling vine tendril ornament"></div>
      <div class="vine-ornament vine-ornament--lower-right" role="img" aria-label="Grey curling vine tendril ornament"></div>
      <div class="vine-ornament vine-ornament--lower-left" role="img" aria-label="Grey curling vine tendril ornament"></div>
      <h2 class="wine-name" style="margin:0;font-weight:400;top:50px;">Every Moonlit Hour</h2>
      <div class="wine-details">
        <p class="wine-details__style">Methode Traditionelle</p>
        <p class="wine-details__style">Blanc de Blancs</p>
        <p class="wine-details__producer">Beyond the Orchards</p>
        <p class="wine-details__region">Adelaide Hills</p>
      </div>
      <div class="vintage" style="top:528px;">2015</div>
    </div>
  </section>

</body>
</html>
```